swimming pool Leak Detection Brochure

I would Like to create a pool leak detection brochure

Target Market(s)

High end Clients with inground swimming pools

Industry/Entity Type

Pool Service

Other font styles liked:
• Im open to suggestions but using my website for ideas is suggested

Colors

Designer to choose colors to be used in the design.

Requirements
Must have
• Do you Have a Leak??
• Figuring out when your pool has a leak can be tough. Environmental factors do play a role in the water level, and just because your pool’s water is lower than normal does not mean it has a leak. Wind, humidity, and sun exposure all impact your rate of evaporation.
• Warning Signs of a Leak in Your Pool
• Your pool, fountain, or spa loses more than 1/4 an inch of water a day
• There are cracks in or around the pool decking
• You need to add water more than once a week
• Grass around the area is soggy
• Your pool deck is sinking or lifting
Nice to have
• PREPARING FOR A LEAK TEST
• To ensure you receive an accurate leak detection test, it is required that you have the pool vacuumed and cleaned beforehand. Dirt and debris in the pool can make it difficult to spot even large leaks. Likewise, the water should be as clear as possible. If your water is green it means mildew, algae, or fungi has infested it. Not only does this make it impossible to test for leaks, but it’s dangerous for our health. Finally our pool should be full to the normal level - we can’t find a leak that is not leaking! After your test, you will be confident knowing you have a pool/fountain/spa that is free of leaks or the Leak has been found and can be repaired Properly.

```html
<!DOCTYPE html>
<html lang="en">
<head>
<meta charset="utf-8">
<title>Clearline Pools – Leak Detection Brochure</title>
<link href="https://fonts.googleapis.com/css2?family=Open+Sans:wght@400;600;700;800&display=swap" rel="stylesheet">
<style>
  :root{
    --backdrop:#1b1b1d;
    --blue:#4e74c2;
    --navy:#23397a;
    --ink-navy:#1f2b68;
    --white:#ffffff;
    --sky:#6f93d4;
    --water:#3d7fb4;
  }
  *{box-sizing:border-box;margin:0;padding:0}
  html,body{width:1200px;height:1200px;overflow:hidden;background:var(--backdrop)}
  body{font-family:"Open Sans",Arial,sans-serif;color:var(--white);position:relative}
  .spread{position:absolute;left:275px;width:659px;height:511px;overflow:hidden}
  .spread--outside{top:51px}
  .spread--inside{top:630px;width:656px}
  .panel{position:absolute;top:0;height:100%;overflow:hidden}
  .photo{position:absolute;left:0;width:100%}
  .band{position:absolute;left:0;width:100%;background:var(--white)}
  .brand-badge{position:absolute;border-radius:50%;background:var(--white);display:flex;align-items:center;justify-content:center;text-align:center;color:var(--navy);font-weight:800;line-height:1.1}
  .body-copy{position:absolute;font-size:11.3px;line-height:15.2px;font-weight:400}
  .contact{position:absolute;left:0;width:100%;text-align:center;font-weight:600;letter-spacing:.3px}
  .headline-strong{position:absolute;font-weight:800;line-height:1}
  .headline-light{position:absolute;font-weight:400;line-height:1}
  .signs{position:absolute;left:10px;top:32px;width:210px;list-style:none;font-size:11.6px;line-height:15.2px}
  .signs li{position:relative;padding-left:14px;margin-bottom:9px}
  .signs li::before{content:"";position:absolute;left:0;top:5px;width:6px;height:6px;background:var(--white)}
</style>
</head>
<body>

<!-- Outside spread -->
<section class="spread spread--outside">
  <div class="panel" style="left:0;width:218px;">
    <div class="photo" role="img" aria-label="Cracked pipe exposed in wet soil, tinted navy" style="top:0;height:100%;background:linear-gradient(180deg,#22306f 0%,#26357a 55%,#3a4470 75%,#5e6680 90%,#3a3f5a 100%);"></div>
    <p class="body-copy" style="left:17px;top:21px;width:198px;">To ensure you receive an accurate leak detection test, it is required that you have the pool vacuumed and cleaned beforehand. Dirt and debris in the pool can make it difficult to spot even large leaks. Likewise, the water should be as clear as possible. If your water is green it means mildew, algae, or fungi has infested it. Not only does this make it impossible to test for leaks, but it’s dangerous for our health. Finally our pool should be full to the normal level - we can’t find a leak that is not leaking! After your test, you will be confident knowing you have a pool/fountain/spa that is free of leaks or the Leak has been found and can be repaired Properly.</p>
  </div>

  <div class="panel" style="left:218px;width:217px;background:var(--blue);">
    <div class="photo" role="img" aria-label="Backyard pool with an inflatable duck floating near trees" style="top:0;height:277px;background:linear-gradient(180deg,#5a84c8 0%,#4a72b8 30%,#2d4a86 55%,#2a4f8f 75%,#3766a8 100%);"></div>
    <div class="band" style="top:278px;height:10px;"></div>
    <div class="brand-badge" style="left:42px;top:220px;width:134px;height:134px;font-size:15px;">Clearline<br>Pools</div>
    <div class="contact" style="top:441px;font-size:21px;">555-014-2290</div>
    <div class="contact" style="top:469px;font-size:13px;">WWW.CLEARLINEPOOLS.COM</div>
  </div>

  <div class="panel" style="left:435px;width:224px;background:var(--blue);">
    <div class="band" style="top:17px;height:11px;"></div>
    <div class="brand-badge" style="left:23px;top:-17px;width:168px;height:168px;font-size:19px;">Clearline<br>Pools</div>
    <div class="headline-strong" style="left:18px;top:183px;font-size:32px;">PREPARING</div>
    <div class="headline-light" style="left:18px;top:218px;font-size:23.5px;">FOR A LEAK TEST</div>
    <div class="photo" role="img" aria-label="Technician testing a spa beside an oceanfront pool deck" style="top:253px;height:258px;background:linear-gradient(180deg,#6f93d4 0%,#9fb9e2 30%,#c9c2b0 50%,#5aa4c8 65%,#3b8ab5 100%);"></div>
  </div>
</section>

<!-- Inside spread -->
<section class="spread spread--inside">
  <div class="panel" style="left:0;width:217px;background:var(--blue);">
    <p class="body-copy" style="left:15px;top:25px;width:196px;">Figuring out when your pool has a leak can be tough. Environmental factors do play a role in the water level, and just because your pool’s water is lower than normal does not mean it has a leak. Wind, humidity, and sun exposure all impact your rate of evaporation.</p>
    <div class="band" style="top:242px;height:13px;"></div>
    <div style="position:absolute;left:45px;top:191px;width:128px;height:128px;border-radius:50%;background:var(--blue);"></div>
    <div role="img" aria-label="Leak detection equipment case with cables and sensors" style="position:absolute;left:52px;top:198px;width:114px;height:114px;border-radius:50%;background:radial-gradient(circle,#e9e9ec 0%,#cfd0d6 55%,#9ea0a8 100%);border:3px solid var(--white);"></div>
    <div class="photo" role="img" aria-label="Technician checking a pool edge at dusk" style="top:344px;height:167px;background:linear-gradient(180deg,#6f8fa0 0%,#3f5e55 35%,#2d4a5e 60%,#2a5576 100%);"></div>
  </div>

  <div class="panel" style="left:217px;width:216px;background:var(--navy);">
    <div class="photo" role="img" aria-label="Inflatable duck floating in a blue pool" style="top:90px;height:120px;background:linear-gradient(90deg,#c9a634 0%,#d9b53e 40%,#3e88c2 70%,#2f78b8 100%);"></div>
    <div class="band" style="top:242px;height:13px;"></div>
    <div class="brand-badge" style="left:43px;top:182px;width:134px;height:134px;font-size:15px;">Clearline<br>Pools</div>
    <div class="headline-strong" style="left:0;width:100%;text-align:center;top:357px;font-size:46px;color:var(--blue);">DO YOU</div>
    <div class="headline-light" style="left:0;width:100%;text-align:center;top:404px;font-size:24px;">HAVE A LEAK??</div>
  </div>

  <div class="panel" style="left:433px;width:223px;background:var(--blue);">
    <ul class="signs" style="top:32px;">
      <li>Warning Signs of a Leak in Your Pool</li>
      <li>Your pool, fountain, or spa loses more than 1/4 an inch of water a day</li>
      <li>There are cracks in or around the pool decking</li>
      <li>You need to add water more than once a week</li>
      <li>Grass around the area is soggy</li>
      <li>Your pool deck is sinking or lifting</li>
    </ul>
    <div class="photo" role="img" aria-label="Infinity pool overlooking the sea with lounge chairs and test kit" style="top:250px;height:261px;background:linear-gradient(180deg,#4e74c2 0%,#8eb0dc 30%,#4a8a6a 45%,#1f6f86 65%,#b7aea0 100%);"></div>
  </div>
</section>

</body>
</html>
```